Buchungsplattform für Hypnose-Dienstleistungen sucht Zertifikat-Design
Zielgruppe
Buchungsplattform für Hypnose Dienstleistungen. Die Zielgruppe des angeklagten Design (Zertifikat) geht an registrierte Anbieter (Hypnosetherapeuten, Praxes, Zahnärzte, etc).
Aufgabenstellung
Das gewünschte Zertifikat soll;
- unser CI/CD berücksichtigen (Primär Orange: #DD3200 Sekundär Blau: #0085A8(
- soll einen wertvollen, aufwendigen, besonderen Eindruck vermitteln
- soll sich inhaltlich in etwa dem angehängten Vorschlag orientieren
- kann spezielle Druckverfahren (Prägedruck, Stanz, Laser, etc. ) in Erwägung ziehen wo angebracht

```html
<!DOCTYPE html>
<html lang="de">
<head>
<meta charset="utf-8">
<title>Certificate of Excellence – Somnara</title>
<link href="https://fonts.googleapis.com/css2?family=Crimson+Pro:wght@400;600&display=swap" rel="stylesheet">
<style>
  :root {
    --orange: #e8501f;
    --ink: #111111;
    --ink-soft: #3a3a3a;
    --paper: #ffffff;
    --beige-light: #f6f2ea;
    --beige-dark: #ece3d2;
    --gold-1: #b8972a;
    --gold-2: #f1e07a;
    --gold-3: #c9a934;
    --frame: #9a9a9a;
  }
  html, body {
    margin: 0;
    padding: 0;
    overflow: hidden;
    background: var(--paper);
  }
  .certificate {
    position: relative;
    width: 848px;
    height: 1200px;
    overflow: hidden;
    background: var(--paper);
    box-sizing: border-box;
    border: 1px solid var(--frame);
    font-family: "Crimson Pro", Georgia, serif;
    color: var(--ink);
  }
  .backdrop {
    position: absolute;
    inset: 0;
    width: 848px;
    height: 1200px;
  }
  .brand {
    position: absolute;
    top: 88px;
    left: 0;
    width: 100%;
    text-align: center;
    font-size: 64px;
    font-weight: 400;
    letter-spacing: 4px;
    color: var(--orange);
    line-height: 1;
  }
  .title {
    position: absolute;
    top: 232px;
    left: 0;
    width: 100%;
    margin: 0;
    text-align: center;
    font-size: 92px;
    font-weight: 600;
    line-height: 94px;
    color: var(--orange);
  }
  .holder {
    position: absolute;
    top: 492px;
    left: 0;
    width: 100%;
    text-align: center;
    font-size: 62px;
    line-height: 1;
  }
  .holder-rule {
    position: absolute;
    top: 573px;
    left: 174px;
    width: 500px;
    height: 1px;
    background: linear-gradient(90deg, transparent, var(--orange) 15%, var(--orange) 85%, transparent);
  }
  .holder-details {
    position: absolute;
    top: 592px;
    left: 0;
    width: 100%;
    text-align: center;
    font-size: 22px;
    line-height: 29px;
    text-transform: uppercase;
  }
  .citation {
    position: absolute;
    top: 674px;
    left: 0;
    width: 100%;
    margin: 0;
    text-align: center;
    font-size: 37px;
    line-height: 46px;
  }
  .issuer-rule {
    position: absolute;
    top: 971px;
    left: 68px;
    width: 264px;
    height: 1px;
    background: linear-gradient(90deg, transparent, var(--orange) 12%, var(--orange) 88%, transparent);
  }
  .issuer {
    position: absolute;
    top: 981px;
    left: 99px;
    font-size: 19px;
    line-height: 24px;
    color: var(--ink-soft);
    text-transform: uppercase;
  }
</style>
</head>
<body>
<main class="certificate">
  <svg class="backdrop" viewBox="0 0 848 1200" aria-hidden="true">
    <defs>
      <linearGradient id="ribbon-gold" x1="0" y1="0" x2="1" y2="1">
        <stop offset="0" stop-color="var(--gold-1)"/>
        <stop offset="0.45" stop-color="var(--gold-2)"/>
        <stop offset="1" stop-color="var(--gold-3)"/>
      </linearGradient>
      <radialGradient id="seal-gold" cx="0.4" cy="0.35" r="0.75">
        <stop offset="0" stop-color="var(--gold-2)"/>
        <stop offset="0.6" stop-color="var(--gold-3)"/>
        <stop offset="1" stop-color="var(--gold-1)"/>
      </radialGradient>
    </defs>
    <polygon class="wedge-light" points="848,728 848,1200 0,1200 0,1188" fill="var(--beige-light)"/>
    <polygon class="wedge-dark" points="0,865 335,1200 0,1200" fill="var(--beige-dark)" opacity="0.85"/>
    <polygon class="ribbon" points="848,800 848,850 516,1200 466,1200" fill="url(#ribbon-gold)"/>
    <circle class="seal" cx="670" cy="1026" r="113" fill="url(#seal-gold)"/>
  </svg>

  <div class="brand">SOMNARA</div>

  <h1 class="title">CERTIFICATE<br>OF EXELLENCE</h1>

  <div class="holder">Praxisname</div>
  <div class="holder-rule"></div>
  <div class="holder-details">
    Vorname&nbsp; Nachname<br>
    Adresse&nbsp;&nbsp; /&nbsp;&nbsp;&nbsp; PLZ Ort
  </div>

  <p class="citation">wird für seine hervorragende Qualität<br>und Betriebsleistung anerkannt.</p>

  <div class="issuer-rule"></div>
  <div class="issuer">Somnara Schweiz AG<br>Quality Assurance</div>
</main>
</body>
</html>
```